Bref créative
Business cards and stationery for innovative cloud apps comapany VORAX
VORAX sa
Use same font as used in my logo
Petros Lamvakis
VP & General Manager
Ermou Ave 27, Kifisia, 14671, Athens, Greece
petros@vorax-mail.gr
www.vorax-mail.gr
In the back we will have the same info in Greek
Name: Πέτρος Λαμβάκης
title: Γενικός Διευθυντής
address: Λεωφ. Ερμού 27, 14671, Κηφισιά, Αθήνα, Ελλάδα
phone: 0030 210 555 0147
cell: 0030 690 555 0293
fax: 0030 210 555 0148
email: petros@vorax-mail.gr
web address: www.vorax-mail.gr

```html
<!DOCTYPE html>
<html lang="en">
<head>
<meta charset="utf-8">
<title>VORAX business cards</title>
<link href="https://fonts.googleapis.com/css2?family=Open+Sans:wght@400;600;700&display=swap" rel="stylesheet">
<style>
  :root {
    --bg: #e6e8ec;
    --card: #ffffff;
    --brand: #2a5db8;
    --ink: #1d2b4a;
    --muted: #5d6472;
    --rule: #c9d3e6;
    --shadow: rgba(20, 30, 50, 0.18);
  }
  * { margin: 0; padding: 0; box-sizing: border-box; }
  html, body { width: 1200px; height: 838px; overflow: hidden; }
  body {
    background: var(--bg);
    font-family: "Open Sans", Arial, sans-serif;
    color: var(--muted);
    display: flex;
    align-items: center;
    justify-content: center;
    gap: 40px;
  }
  .card {
    position: relative;
    width: 540px;
    height: 310px;
    background: var(--card);
    border-radius: 14px;
    box-shadow: 0 12px 30px var(--shadow);
    overflow: hidden;
  }
  .brand {
    position: absolute;
    left: 36px;
    top: 112px;
    display: flex;
    align-items: center;
    gap: 12px;
  }
  .brand-dot {
    width: 22px; height: 22px;
    border-radius: 50%;
    background: var(--brand);
  }
  .brand-name {
    font-size: 56px;
    font-weight: 700;
    letter-spacing: 2px;
    color: var(--brand);
    line-height: 1;
  }
  .details {
    position: absolute;
    left: 300px;
    top: 62px;
    width: 220px;
  }
  .person-name {
    font-size: 17px;
    font-weight: 700;
    color: var(--ink);
    line-height: 1.2;
  }
  .person-title {
    font-size: 10.5px;
    color: var(--muted);
    margin-bottom: 14px;
  }
  .address {
    font-size: 10.5px;
    line-height: 1.45;
    margin-bottom: 14px;
  }
  .contacts { list-style: none; }
  .contacts li {
    display: flex;
    align-items: center;
    gap: 7px;
    font-size: 10.5px;
    line-height: 1.7;
  }
  .contacts svg { width: 11px; height: 11px; fill: var(--ink); flex: none; }
  .web-line {
    position: absolute;
    left: 36px;
    right: 70px;
    bottom: 30px;
    display: flex;
    align-items: center;
    gap: 12px;
    font-size: 10px;
    color: var(--muted);
  }
  .web-line::after {
    content: "";
    flex: 1;
    height: 1px;
    background: var(--rule);
  }
  .corner-dot {
    position: absolute;
    right: 30px;
    bottom: 24px;
    width: 20px; height: 20px;
    border-radius: 50%;
    background: var(--brand);
  }
</style>
</head>
<body>
  <svg width="0" height="0" style="position:absolute">
    <defs>
      <symbol id="icon-phone" viewBox="0 0 24 24"><path d="M6.6 10.8a15.1 15.1 0 0 0 6.6 6.6l2.2-2.2a1 1 0 0 1 1-.25 11.4 11.4 0 0 0 3.6.57 1 1 0 0 1 1 1V20a1 1 0 0 1-1 1A17 17 0 0 1 3 4a1 1 0 0 1 1-1h3.5a1 1 0 0 1 1 1c0 1.25.2 2.45.57 3.57a1 1 0 0 1-.25 1z"/></symbol>
      <symbol id="icon-mobile" viewBox="0 0 24 24"><path d="M7 1h10a2 2 0 0 1 2 2v18a2 2 0 0 1-2 2H7a2 2 0 0 1-2-2V3a2 2 0 0 1 2-2zm0 3v14h10V4zm5 15.5a1.2 1.2 0 1 0 0 2.4 1.2 1.2 0 0 0 0-2.4z"/></symbol>
      <symbol id="icon-fax" viewBox="0 0 24 24"><path d="M6 2h12v5H6zM3 8h18a2 2 0 0 1 2 2v7h-4v5H5v-5H1v-7a2 2 0 0 1 2-2zm4 8v4h10v-4z"/></symbol>
      <symbol id="icon-mail" viewBox="0 0 24 24"><path d="M2 4h20a1 1 0 0 1 1 1v14a1 1 0 0 1-1 1H2a1 1 0 0 1-1-1V5a1 1 0 0 1 1-1zm1 2.2V18h18V6.2l-9 6.3z"/></symbol>
    </defs>
  </svg>

  <article class="card card-front" lang="en">
    <div class="brand"><span class="brand-name">VORAX</span></div>
    <div class="details">
      <p class="person-name">Petros Lamvakis</p>
      <p class="person-title">VP &amp; General Manager</p>
      <p class="address">Ermou Ave 27, Kifisia,<br>14671, Athens, Greece</p>
      <ul class="contacts">
        <li><svg><use href="#icon-phone"/></svg>0030 210 555 0147</li>
        <li><svg><use href="#icon-mobile"/></svg>0030 690 555 0293</li>
        <li><svg><use href="#icon-fax"/></svg>0030 210 555 0148</li>
        <li><svg><use href="#icon-mail"/></svg>petros@vorax-mail.gr</li>
      </ul>
    </div>
    <div class="web-line">www.vorax-mail.gr</div>
    <span class="corner-dot"></span>
  </article>

  <article class="card card-back" lang="el">
    <div class="brand"><span class="brand-name">VORAX</span></div>
    <div class="details">
      <p class="person-name">Πέτρος Λαμβάκης</p>
      <p class="person-title">Γενικός Διευθυντής</p>
      <p class="address">Λεωφ. Ερμού 27, 14671, Κηφισιά,<br>Αθήνα, Ελλάδα</p>
      <ul class="contacts">
        <li><svg><use href="#icon-phone"/></svg>0030 210 555 0147</li>
        <li><svg><use href="#icon-mobile"/></svg>0030 690 555 0293</li>
        <li><svg><use href="#icon-fax"/></svg>0030 210 555 0148</li>
        <li><svg><use href="#icon-mail"/></svg>petros@vorax-mail.gr</li>
      </ul>
    </div>
    <div class="web-line">www.vorax-mail.gr</div>
    <span class="corner-dot"></span>
  </article>
</body>
</html>
```